Business Card Design Project used as hotel key

I need a project to be printed on PVC card and used by our customers as room key.

The design and the color are up to you. My idea would be to include the logo (colour can also be changed) on the front side and our Internet address on the back (http://www.valmirenza.ch, info@valmirenza.ch).

Target Market(s)

Hôtel customers

Industry/Entity Type

Hotel

Requirements
Must have
• I have attached below the template of the front and back of the card. The logo on the back shown on the template below the magnetic stripe should not be used.

Must have:

1. Follow the template size (shown in the template):

Full Bleed Size:
3.55" x 2.3"
90.17mm x 58.42mm
1065 x 690 pixels

Trim Size:
3.375" x 2.125"
85.77mm x 54.02mm
1013 x 638 pixels

A bleed is the outer area of your artwork that falls on the outside of the trim line. It is important that you do not have any important information in the bleed area as ¼ “ will be cut off on all sides. Cards with a “framed border” are not recommended due to variances in die cutting.

2. Make sure you leave the area between the magstripe markers on the template blank.

3. There need to be an arrow on the front side (on the left), pointing the left side

4. Color: Full color both sides, color process CMYK. 300 DPI at 100% of the final print size

```html
<!DOCTYPE html>
<html lang="en">
<head>
<meta charset="utf-8">
<title>Hôtel Valmirenza – Room Keycard</title>
<link rel="stylesheet" href="https://fonts.googleapis.com/css2?family=Jost:wght@400;500;700&display=swap">
<style>
  :root {
    --backdrop: #ece8e6;
    --card-black: #141113;
    --card-texture: #262124;
    --mauve: #8c5d6c;
    --band-ink: #141113;
    --white: #ffffff;
    --icon-fill: #d9d4d6;
  }
  * { box-sizing: border-box; margin: 0; padding: 0; }
  html, body {
    width: 1200px; height: 778px; overflow: hidden;
    background: var(--backdrop);
    font-family: "Jost", "Futura", sans-serif;
  }
  .sheet {
    position: relative; width: 1200px; height: 778px;
    display: flex; align-items: center; justify-content: center; gap: 40px;
  }
  .keycard {
    position: relative; width: 540px; height: 340px;
    border-radius: 14px; overflow: hidden;
    background: radial-gradient(ellipse at 55% 50%, var(--card-texture) 0%, var(--card-black) 70%);
    box-shadow: 0 6px 18px rgba(0,0,0,.25);
  }
  /* front */
  .keycard-front { display: flex; align-items: center; justify-content: center; }
  .insert-arrow {
    position: absolute; left: 26px; top: 50%;
    width: 40px; height: 28px; transform: translateY(-50%);
  }
  .wordmark {
    display: flex; align-items: center; gap: 14px;
    color: var(--mauve); font-weight: 500;
    font-size: 44px; line-height: 1; white-space: nowrap;
  }
  .wordmark-dot { width: 18px; height: 18px; border-radius: 50%; background: var(--mauve); flex: none; }
  /* back */
  .magstripe-band {
    position: absolute; left: 0; right: 0; top: 44px; height: 64px;
    background: var(--mauve);
    display: flex; align-items: center; justify-content: center;
  }
  .magstripe-band h2 {
    font-size: 30px; font-weight: 700; letter-spacing: 4px;
    color: var(--band-ink); text-transform: uppercase;
  }
  .steps {
    position: absolute; left: 60px; right: 60px; top: 128px;
    display: grid; grid-template-columns: repeat(4, 1fr); gap: 12px 18px;
  }
  .step-diagram {
    height: 46px; border-radius: 4px;
    background: linear-gradient(135deg, var(--icon-fill), #9f9a9c);
    opacity: .85;
  }
  .instructions {
    position: absolute; left: 0; right: 0; top: 246px;
    text-align: center; color: var(--white); font-size: 16px; line-height: 1.35;
  }
  .bullet {
    display: inline-block; width: 6px; height: 6px; border-radius: 50%;
    background: var(--mauve); margin: 0 6px 0 8px; vertical-align: middle;
  }
  .contacts {
    position: absolute; left: 0; right: 0; bottom: 20px;
    display: flex; justify-content: center; gap: 28px;
    color: var(--white); font-size: 15px;
  }
  .contact { display: flex; align-items: center; gap: 6px; }
  .contact svg { width: 12px; height: 12px; }
</style>
</head>
<body>
<main class="sheet">
  <section class="keycard keycard-front" aria-label="Keycard front">
    <svg class="insert-arrow" viewBox="0 0 40 28" aria-label="Insert this end first">
      <path d="M2 14 L16 2 L16 9 L38 9 L38 19 L16 19 L16 26 Z" fill="var(--mauve)"/>
    </svg>
    <div class="wordmark">
      <span class="wordmark-dot"></span>
      <span class="wordmark-name">Hôtel Valmirenza</span>
    </div>
  </section>

  <section class="keycard keycard-back" aria-label="Keycard back">
    <div class="magstripe-band"><h2>Magnetic Stripe</h2></div>
    <div class="steps">
      <div class="step-diagram" role="img" aria-label="Diagram: keycard inserted into door lock"></div>
      <div class="step-diagram" role="img" aria-label="Diagram: keycard swiped through reader"></div>
      <div class="step-diagram" role="img" aria-label="Diagram: hand holding keycard at reader"></div>
      <div class="step-diagram" role="img" aria-label="Diagram: keycard in slot reader"></div>
      <div class="step-diagram" role="img" aria-label="Diagram: lock with keycard removed"></div>
      <div class="step-diagram" role="img" aria-label="Diagram: hand removing keycard"></div>
      <div class="step-diagram" role="img" aria-label="Diagram: door handle pressed"></div>
      <div class="step-diagram" role="img" aria-label="Diagram: hand opening the door"></div>
    </div>
    <p class="instructions">
      <span class="bullet"></span>Fully insert or swipe Keycard<span class="bullet"></span>Remove Keycard<br>
      <span class="bullet"></span>Depress handle and open door
    </p>
    <div class="contacts">
      <span class="contact">
        <svg viewBox="0 0 12 12" aria-hidden="true"><circle cx="6" cy="6" r="5" fill="none" stroke="var(--mauve)" stroke-width="1.6"/><circle cx="6" cy="6" r="1.8" fill="var(--mauve)"/></svg>
        www.valmirenza.ch
      </span>
      <span class="contact">
        <svg viewBox="0 0 12 12" aria-hidden="true"><rect x="0.8" y="2.5" width="10.4" height="7" fill="var(--mauve)"/><path d="M1 3 L6 7 L11 3" fill="none" stroke="var(--card-black)" stroke-width="1"/></svg>
        info@valmirenza.ch
      </span>
    </div>
  </section>
</main>
</body>
</html>
```